Rack Card Design for an Ayurvedic Beauty Product Project

Hello, I need to have rack cards. The rack cards would be about 3 products we are showcasing at an event. I am a cosmetic company. I have a logo and basic design ideas. I have attached some product images and info. By no means am I a designer so please excuse my messy AI files. Please feel free to design this as feminine as you like. :)

Target Market(s)

Beauty industry, organic, holistic, ayurveda

Industry/Entity Type

Cosmetic

```html
<!DOCTYPE html>
<html lang="en">
<head>
<meta charset="utf-8">
<title>Amber Bloom Rack Cards</title>
<link href="https://fonts.googleapis.com/css2?family=Quicksand:wght@400;500;600&display=swap" rel="stylesheet">
<style>
  :root {
    --backdrop: #d0d0d0;
    --plum-light: #862a66;
    --plum-dark: #4c0c3a;
    --cream: #f6ecc8;
    --gold: #b8894a;
    --gold-light: #e2c487;
    --ink: #222;
    --white: #fff;
  }
  * { margin: 0; padding: 0; box-sizing: border-box; }
  html, body { width: 1200px; height: 1200px; overflow: hidden; }
  body { background: var(--backdrop); font-family: "Quicksand", sans-serif; position: relative; }
  .rack-card {
    position: absolute; top: 206px; width: 355px; height: 774px;
    background: var(--white); overflow: hidden;
  }
  .rack-card--cream { left: 52px; }
  .rack-card--serum { left: 423px; }
  .rack-card--toner { left: 794px; }
  .card-backdrop { position: absolute; inset: 0; width: 355px; height: 774px; }
  .brand { position: absolute; top: 54px; left: 0; width: 100%; text-align: center; }
  .brand-dot {
    display: block; width: 58px; height: 58px; margin: 0 auto 18px;
    border-radius: 50%; background: var(--gold);
  }
  .brand-name {
    color: var(--gold-light); font-weight: 600; font-size: 12.5px; letter-spacing: 0.6px;
    text-transform: uppercase;
  }
  .product-title {
    position: absolute; top: 186px; left: 0; width: 100%; text-align: center;
    color: var(--white); font-weight: 400; font-size: 31px; line-height: 38px;
  }
  .product-shot { position: absolute; }
  .rack-card--cream .product-shot {
    left: 104px; top: 358px; width: 158px; height: 260px; border-radius: 40px 40px 30px 30px;
    background: linear-gradient(180deg, var(--gold-light) 0 18%, #f2f2f2 18% 30%, var(--plum-light) 30% 90%, #f2f2f2 90%);
  }
  .rack-card--serum .product-shot {
    left: 137px; top: 330px; width: 84px; height: 268px; border-radius: 4px 4px 10px 10px;
    background: linear-gradient(180deg, #7a1f5e 0 72%, var(--gold-light) 72%, var(--gold) 100%);
  }
  .rack-card--toner .product-shot {
    left: 113px; top: 326px; width: 136px; height: 284px; border-radius: 4px 4px 14px 14px;
    background: linear-gradient(180deg, #8a2a6c 0 70%, var(--gold-light) 70%, var(--gold) 100%);
  }
  .product-copy {
    position: absolute; left: 0; width: 100%; text-align: center;
    color: var(--ink); font-size: 13.2px; line-height: 17px; padding: 0 30px;
  }
  .rack-card--cream .product-copy { top: 662px; }
  .rack-card--serum .product-copy { top: 622px; }
  .rack-card--toner .product-copy { top: 640px; }
</style>
</head>
<body>
  <section class="rack-card rack-card--cream">
    <svg class="card-backdrop" viewBox="0 0 355 774" aria-hidden="true">
      <defs>
        <linearGradient id="plum1" x1="0" y1="0" x2="1" y2="1">
          <stop offset="0" stop-color="#862a66"/><stop offset="1" stop-color="#4c0c3a"/>
        </linearGradient>
      </defs>
      <path d="M0 0H355V242C300 360 180 428 0 432Z" fill="url(#plum1)"/>
      <path d="M0 432C180 428 300 360 355 242V290C300 400 180 460 0 466Z" fill="#f6ecc8"/>
    </svg>
    <div class="brand"><span class="brand-dot"></span><p class="brand-name">Amber Bloom</p></div>
    <h2 class="product-title">Ayurvedic<br>Firming &amp; Lifting<br>Breast Cream</h2>
    <div class="product-shot" role="img" aria-label="Frosted jar of firming breast cream with gold lid"></div>
    <p class="product-copy">Using all natural Ayurvedic herbs, our breast cream helps enhance, tighten, and lift your breast.</p>
  </section>

  <section class="rack-card rack-card--serum">
    <svg class="card-backdrop" viewBox="0 0 355 774" aria-hidden="true">
      <defs>
        <linearGradient id="plum2" x1="0" y1="0" x2="1" y2="1">
          <stop offset="0" stop-color="#862a66"/><stop offset="1" stop-color="#4c0c3a"/>
        </linearGradient>
      </defs>
      <path d="M0 0H355V242C300 360 180 428 0 432Z" fill="url(#plum2)"/>
      <path d="M0 432C180 428 300 360 355 242V290C300 400 180 460 0 466Z" fill="#f6ecc8"/>
    </svg>
    <div class="brand"><span class="brand-dot"></span><p class="brand-name">Amber Bloom</p></div>
    <h2 class="product-title">Ayurvedic<br>Firming &amp; Toning<br>Breast Serum</h2>
    <div class="product-shot" role="img" aria-label="Slim plum tube of toning breast serum with gold cap"></div>
    <p class="product-copy">Using all natural Ayurvedic herbs, and a touch of 24k gold, our serum enhances the experience and quality of results when partnered with the Amber Bloom Firming and Lifting Breast Cream providing an all-day boosting experience</p>
  </section>

  <section class="rack-card rack-card--toner">
    <svg class="card-backdrop" viewBox="0 0 355 774" aria-hidden="true">
      <defs>
        <linearGradient id="plum3" x1="0" y1="0" x2="1" y2="1">
          <stop offset="0" stop-color="#862a66"/><stop offset="1" stop-color="#4c0c3a"/>
        </linearGradient>
      </defs>
      <path d="M0 0H355V242C300 360 180 428 0 432Z" fill="url(#plum3)"/>
      <path d="M0 432C180 428 300 360 355 242V290C300 400 180 460 0 466Z" fill="#f6ecc8"/>
    </svg>
    <div class="brand"><span class="brand-dot"></span><p class="brand-name">Amber Bloom</p></div>
    <h2 class="product-title">Ayurvedic<br>Firming &amp; Lifting<br>Breast Toner</h2>
    <div class="product-shot" role="img" aria-label="Wide plum tube of lifting breast toner with gold cap"></div>
    <p class="product-copy">Using all natural Ayurvedic herbs, our breast toner, prepares the area for maximum absorption giving you the best results and the most invigorating treatment.</p>
  </section>
</body>
</html>
```